PowerPoint Design Project

Kestrel Estate Group is a Melbourne based property development management company. We provide a comprehensive range of development management services to a select group of listed developers, private landowners, overseas investors and development partners and institutional clients. Our website provides additional information about the company:
http://www.kestreleg.com.au
We are looking for a versatile powerpoint design that can be used across a wide variety of presentations including; pitch documents, client reports, Information memorandums, and downloadable credential packs etc. We have attached a good example document.
Updates

Industry/Entity Type

It Company

Requirements
Must have
• The design should have the following slides as a minimum: Intro Page, transition slides, profile slides, slides for graphics,

```html
<!DOCTYPE html>
<html lang="en">
<head>
<meta charset="utf-8">
<title>Kestrel Estate Group – Presentation Template</title>
<link href="https://fonts.googleapis.com/css2?family=Open+Sans:ital,wght@0,400;0,600;0,700;0,800;1,700&family=Arimo:wght@400;700&display=swap" rel="stylesheet">
<style>
:root{
  --bg:#e6e1d8;
  --paper:#ffffff;
  --ink:#111111;
  --body:#6a6a6a;
  --band:#0d0d0d;
  --swoosh:#a9a9a9;
  --cyl-top:#151515;
  --cyl-side:#9a9a9a;
  --cyl-light:#d6d6d6;
}
*{margin:0;padding:0;box-sizing:border-box}
html,body{width:1200px;height:433px;overflow:hidden;background:var(--bg)}
body{position:relative;font-family:"Open Sans",Arial,sans-serif;color:var(--ink)}
.slide{position:absolute;width:267px;height:199px;background:var(--paper);overflow:hidden;box-shadow:0 1px 3px rgba(0,0,0,.25)}
.footer{position:absolute;left:0;bottom:0;width:267px;height:18px}
.footer-url{position:absolute;right:12px;bottom:2px;font-size:6.2px;color:#fff;letter-spacing:.5px}
.heading{position:absolute;left:13px;top:11px;font-size:11px;font-weight:400;letter-spacing:.1px}
.copy{position:absolute;font-size:4.6px;line-height:6.6px;color:var(--body);text-align:justify}
.brand{position:absolute;left:0;width:267px;display:flex;justify-content:center;align-items:center;gap:5px}
.brand-mark{width:9px;height:9px;background:var(--ink)}
.brand-name{font-weight:800;font-size:13px;letter-spacing:.3px;color:var(--ink)}
.photo{position:absolute;border:1px solid #9a9a9a}
.title{position:absolute;left:0;width:267px;text-align:center;font-family:"Arimo",Arial,sans-serif;font-weight:700}
.subtitle{font-size:5.4px;font-weight:600;color:var(--ink);margin-bottom:1px}
.table-cell{position:absolute;width:115px}
.table-cell p{font-size:5.4px;line-height:7px;color:#333}
.chart{position:absolute;left:0;top:0}
.contact{position:absolute;left:0;width:267px;text-align:center;font-size:4.8px;line-height:8px;color:#222}
.contact b{font-style:italic;font-weight:700}
</style>
</head>
<body>

<svg width="0" height="0" style="position:absolute" aria-hidden="true">
  <defs>
    <symbol id="slide-footer" viewBox="0 0 267 18">
      <path d="M0 12 C60 11 110 10 140 8 L267 8 L267 18 L0 18 Z" fill="var(--swoosh)"/>
      <path d="M0 15 C70 14 120 13 145 8 C150 6 155 6 160 6 L267 6 L267 18 L0 18 Z" fill="var(--band)"/>
    </symbol>
    <linearGradient id="cyl-grad" x1="0" x2="1">
      <stop offset="0" stop-color="var(--cyl-side)"/>
      <stop offset=".45" stop-color="var(--cyl-light)"/>
      <stop offset="1" stop-color="var(--cyl-side)"/>
    </linearGradient>
    <g id="cylinder">
      <rect x="0" y="4" width="34" height="22" fill="url(#cyl-grad)"/>
      <ellipse cx="17" cy="26" rx="17" ry="4" fill="url(#cyl-grad)"/>
      <ellipse cx="17" cy="4" rx="17" ry="4" fill="var(--cyl-top)"/>
      <text x="17" y="18" font-size="4.6" font-weight="700" fill="#fff" text-anchor="middle" font-family="Open Sans, sans-serif">Lorem</text>
    </g>
    <g id="head-box">
      <rect width="42" height="17" rx="3" fill="var(--cyl-top)"/>
      <text x="21" y="10.5" font-size="4.6" font-weight="700" fill="#fff" text-anchor="middle" font-family="Open Sans, sans-serif">Lorem ipsum</text>
    </g>
  </defs>
</svg>

<!-- Cover -->
<section class="slide" style="left:19px;top:6px">
  <div class="brand" style="top:82px"><span class="brand-mark"></span><span class="brand-name">KESTREL ESTATE GROUP</span></div>
  <div class="title" style="top:129px;font-size:15px">Title of Presentation</div>
  <svg class="footer"><use href="#slide-footer"/></svg>
  <span class="footer-url">www.kestrelestate.com</span>
</section>

<!-- Intro -->
<section class="slide" style="left:320px;top:6px">
  <h2 class="heading">INTRO PAGE</h2>
  <p class="copy" style="left:13px;top:30px;width:241px">Lorem ipsum d olor sit amet, consectetuer adipiscing elit, sed diam nonummy nibh euismod tincidunt ut laoreet dolore magna aliquam erat volutpat. Ut wisi enim ad minim veniam, quis nostrud exerci tation ullamcorper suscipit lobortis nisl ut aliquip ex ea commodo consequat. Duis autem vel eum iriure dolor in hendrerit in vulputate velit esse molestie consequat, vel illum dolore eu feugiat nulla facilisis.</p>
  <p class="copy" style="left:13px;top:74px;width:135px">Lorem ipsum d olor sit amet, consectetuer adipiscing elit, sed diam nonummy nibh euismod tincidunt ut laoreet dolore magnae consequat, vel illum dolore eu feugiat nulla facilisis.</p>
  <p class="copy" style="left:13px;top:118px;width:135px">Lorem ipsum d olor sit amet, consectetuer adipiscing elit, sed diam nonummy nibh euismod tincidunt ut laoreet dolore magna aliquam erat volutpat. Ut wisi enim ad minim veniam, quis nostrud exerci tation ullamcorper suscipit lobortis nisl ut aliquip ex ea commodo consequat.</p>
  <div class="photo" role="img" aria-label="Photo of a modern interior with a red staircase" style="left:161px;top:93px;width:97px;height:54px;background:linear-gradient(90deg,#cfcfcf 0%,#b83a34 35%,#d9d9d9 60%,#efefef 100%)"></div>
  <svg class="footer"><use href="#slide-footer"/></svg>
  <span class="footer-url">www.kestrelestate.com</span>
</section>

<!-- Graphics -->
<section class="slide" style="left:618px;top:6px">
  <h2 class="heading">SLIDES FOR GRAPHICS</h2>
  <svg class="chart" width="267" height="199" aria-label="Column diagram">
    <g stroke="#bdbdbd" stroke-width=".6" fill="none">
      <path d="M39 49 H34 V120 H46"/>
      <path d="M81 85 H107 M81 117 H107 M131 85 H157 M131 117 H157 M181 85 H207 M181 117 H207 M131 149 H157 M181 149 H207"/>
    </g>
    <use href="#head-box" x="39" y="40"/>
    <use href="#head-box" x="90" y="40"/>
    <use href="#head-box" x="140" y="40"/>
    <use href="#head-box" x="190" y="40"/>
    <use href="#cylinder" x="46" y="68"/>
    <use href="#cylinder" x="46" y="101"/>
    <use href="#cylinder" x="97" y="68"/>
    <use href="#cylinder" x="97" y="101"/>
    <use href="#cylinder" x="97" y="133"/>
    <use href="#cylinder" x="147" y="68"/>
    <use href="#cylinder" x="147" y="101"/>
    <use href="#cylinder" x="147" y="133"/>
    <use href="#cylinder" x="197" y="68"/>
    <use href="#cylinder" x="197" y="101"/>
    <use href="#cylinder" x="197" y="133"/>
  </svg>
  <svg class="footer"><use href="#slide-footer"/></svg>
  <span class="footer-url">www.kestrelestate.com</span>
</section>

<!-- Table -->
<section class="slide" style="left:918px;top:6px">
  <h2 class="heading">SLIDES FOR TABLE</h2>
  <div class="table-cell" style="left:12px;top:35px"><div class="subtitle">Sub Title-1</div><p>Lorem ipsum dolor sit amet, etuer.Lorem ipsum dolor sit amet, etuer.Lorem ipsum dolor sit amet, etuer.Lorem ipsum dolor</p></div>
  <div class="table-cell" style="left:144px;top:35px"><div class="subtitle">Sub Title-1</div><p>Lorem ipsum dolor sit amet, etuer.Lorem ipsum dolor sit amet, etuer.Lorem ipsum dolor sit amet, etuer.Lorem ipsum dolor</p></div>
  <div class="table-cell" style="left:12px;top:81px"><div class="subtitle">Sub Title-2</div><p>Lorem ipsum dolor sit amet, etuer.Lorem ipsum dolor sit amet, etuer.Lorem ipsum dolor sit amet, etuer.Lorem ipsum dolor</p></div>
  <div class="table-cell" style="left:144px;top:81px"><div class="subtitle">Sub Title-2</div><p>Lorem ipsum dolor sit amet, etuer.Lorem ipsum dolor sit amet, etuer.Lorem ipsum dolor sit amet, etuer.Lorem ipsum dolor</p></div>
  <div class="table-cell" style="left:12px;top:127px"><div class="subtitle">Sub Title-3</div><p>Lorem ipsum dolor sit amet, etuer.Lorem ipsum dolor sit amet, etuer.Lorem ipsum dolor sit amet, etuer.Lorem ipsum dolor</p></div>
  <div class="table-cell" style="left:144px;top:127px"><div class="subtitle">Sub Title-3</div><p>Lorem ipsum dolor sit amet, etuer.Lorem ipsum dolor sit amet, etuer.Lorem ipsum dolor sit amet, etuer.Lorem ipsum dolor</p></div>
  <svg class="footer"><use href="#slide-footer"/></svg>
  <span class="footer-url">www.kestrelestate.com</span>
</section>

<!-- Transition -->
<section class="slide" style="left:19px;top:223px">
  <h2 class="heading">TRANSITION SLIDES</h2>
  <div class="title" style="top:61px;font-size:16px">PART 3</div>
  <p class="copy" style="left:50px;top:85px;width:167px;text-align:center">Orem ipsum dolor sit amet, consectetuer adipiscing elit, sed diam nonummy nibh euismod tincidunt ut laoreet dolore magna aliquam erat volutpat. Ut wisi enim ad minim veniam, quis nostrud exerci tation ullamcorper suscipit lobortis nisl ut aliquip ex ea commodo consequat. Duis autem vel eum iriure dolor in hendrerit in</p>
  <svg class="footer"><use href="#slide-footer"/></svg>
  <span class="footer-url">www.kestrelestate.com</span>
</section>

<!-- Profile -->
<section class="slide" style="left:320px;top:223px">
  <h2 class="heading">PROFILE SLIDES</h2>
  <p class="copy" style="left:16px;top:56px;width:105px">Lorem ipsum dolor sit amet, consectetuer adipiscing elit, sed diam nonummy nibh euismod tincidunt ut laoreet dolore magna aliquam erat volutpat. Ut wisi enim ad minim veniam, quis nostrud exerci tation ullamcorper suscipit lobortis nisl ut aliquip ex ea commodo consequat. Duis autem vel eum iri. Lorem ipsum dolor sit amet, consectetuer adipiscing elit, sed diam nonummy nibh euismod</p>
  <div class="photo" role="img" aria-label="Portrait photo of a smiling business team" style="left:134px;top:58px;width:122px;height:93px;background:linear-gradient(180deg,#f2f2f2 0%,#d8c4b4 40%,#3a3a3e 100%)"></div>
  <svg class="footer"><use href="#slide-footer"/></svg>
  <span class="footer-url">www.kestrelestate.com</span>
</section>

<!-- Content -->
<section class="slide" style="left:618px;top:223px">
  <h2 class="heading">LOREM IPSUM</h2>
  <p class="copy" style="left:27px;top:34px;width:213px;text-align:left">Orem ipsum dolor sit amet, consectetuer adipiscing elit, sed diam nonummy nibh euismod tincidunt ut laoreet dolore magna aliquam erat volutpat. Ut wisi enim ad minim veniam, quis nostrud exerci tation ullamcorper suscipit lobortis nisl ut aliquip ex ea commodo consequat.</p>
  <div class="photo" role="img" aria-label="Photo of a family in front of a house with a red roof" style="left:27px;top:78px;width:112px;height:96px;background:linear-gradient(180deg,#c43a2c 0%,#e9e2da 45%,#a9a4a0 100%)"></div>
  <div class="photo" role="img" aria-label="Photo of a smiling woman holding a bank card" style="left:143px;top:78px;width:96px;height:96px;background:linear-gradient(135deg,#f4f4f4 0%,#d9b79c 50%,#8c5a3c 100%)"></div>
  <svg class="footer"><use href="#slide-footer"/></svg>
  <span class="footer-url">www.kestrelestate.com</span>
</section>

<!-- Closing -->
<section class="slide" style="left:918px;top:223px">
  <div class="brand" style="top:50px"><span class="brand-mark"></span><span class="brand-name">KESTREL ESTATE GROUP</span></div>
  <div class="title" style="top:94px;font-size:13px;line-height:16px;font-style:italic">THANK YOU<br>FOR ATTENTION</div>
  <div class="contact" style="top:150px"><b>phone:</b> 020 4100 2270 &nbsp;<b>Fax:</b> 020 4100 2271<br>14 Harlow Lane, London W2 4QT</div>
  <svg class="footer"><use href="#slide-footer"/></svg>
  <span class="footer-url">www.kestrelestate.com</span>
</section>

</body>
</html>
```